Power point Presentation Template 2

I am looking a professionally designed Powerpoint Presentation template for my company. We are Information Technology Company. I have attached the Logo. The Logo will also give an indication of which colours to be used in the design.

Target Market(s)

Information and Communication Technology

Requirements
Must have
• All ideas welcomed
Nice to have
• Professional Look and Feel

```html
<!DOCTYPE html>
<html lang="en">
<head>
<meta charset="utf-8">
<title>Nexora Technologies – Presentation Template</title>
<link href="https://fonts.googleapis.com/css2?family=Arimo:wght@400;700&display=swap" rel="stylesheet">
<style>
:root{
  --orange:#f47a20;
  --orange-deep:#e8660f;
  --dark:#2b2b2b;
  --grey:#dcdcdc;
  --grey-light:#efefef;
  --canvas:#bfe1fb;
  --ink:#222;
  --muted:#555;
}
*{box-sizing:border-box}
html,body{margin:0;padding:0}
body{width:1044px;height:1200px;overflow:hidden;background:var(--canvas);font-family:'Arimo',Arial,sans-serif;position:relative;color:var(--ink)}
.slide{position:absolute;width:326px;height:184px;background:#fff;overflow:hidden}
.slide>*{position:absolute}
.footer{left:0;right:0;bottom:0;height:6px;background:var(--orange);font-size:3px;color:#fff;text-align:center;line-height:6px;letter-spacing:.2px}
.footer .pg{position:absolute;right:0;top:0;width:30px;height:6px;background:var(--dark);text-align:right;padding-right:3px}
.mark{top:5px;right:6px;font-size:6px;font-weight:700;color:var(--orange);z-index:3}
.txt{font-size:3.6px;line-height:1.65;color:var(--muted);text-align:justify;margin:0}
.h-slide{font-weight:700;color:var(--ink);margin:0;line-height:1.1}
.photo{border:0}
.vert{transform:rotate(-90deg);transform-origin:left top;white-space:nowrap;color:#fff;font-weight:700}
.tab{background:var(--orange);color:#fff;font-weight:700;font-size:13px;text-align:center;line-height:24px}
.bullets{list-style:none;margin:0;padding:0}
.bullets li{position:relative;padding-left:12px;margin-bottom:6px;font-size:3.6px;line-height:1.65;color:var(--muted)}
.bullets li::before{content:"";position:absolute;left:0;top:1px;border-left:6px solid var(--orange);border-top:3.5px solid transparent;border-bottom:3.5px solid transparent}
.box-head{height:9px;background:var(--orange);color:#fff;font-size:4.2px;font-weight:700;text-align:center;line-height:9px}
.box-body{padding:2px;border:.5px solid #eee}
.dot{position:absolute;width:31px;height:31px;border-radius:50%}
</style>
</head>
<body>

<section class="slide cover-dark" style="left:16px;top:15px">
  <div class="mark">NEXORA</div>
  <div class="photo" role="img" aria-label="Dark space scene with glowing network points" style="left:0;top:16px;width:326px;height:134px;background:radial-gradient(ellipse at 65% 60%,#6b5a2c 0%,#1d2a40 40%,#0b1422 80%)"></div>
  <h1 class="h-slide" style="left:0;width:326px;top:64px;text-align:center;color:#fff;font-size:20px">PRESENTATION TITLE</h1>
  <div style="left:0;width:326px;top:85px;text-align:center;color:#fff;font-size:15px">Sub title goes here</div>
  <div style="left:0;width:326px;top:155px;text-align:center;color:var(--orange);font-weight:700;font-size:11px">NEXORA TECHNOLOGIES</div>
  <div class="footer">NEXORA TECHNOLOGIES<span class="pg">1</span></div>
</section>

<section class="slide cover-photo" style="left:361px;top:15px">
  <svg style="left:0;top:0" width="326" height="184" role="img" aria-label="Hand holding a tablet with a glowing network of people icons">
    <defs><linearGradient id="g2" x1="0" y1="0" x2="1" y2="1"><stop offset="0" stop-color="#1e3550"/><stop offset=".5" stop-color="#7a4a2a"/><stop offset="1" stop-color="#1a2436"/></linearGradient></defs>
    <polygon points="14,11 212,11 225,22 314,22 314,172 80,172 70,184 14,184" fill="url(#g2)"/>
    <polygon points="14,73 200,73 213,97 200,121 14,121" fill="#fff"/>
  </svg>
  <h1 class="h-slide" style="left:22px;top:82px;color:var(--orange);font-size:16px">PRESENTATION TITLE</h1>
  <div style="left:54px;top:99px;color:var(--orange);font-size:13px">Sub title goes here</div>
  <div style="left:22px;top:172px;background:#fff;padding:0 4px;color:var(--orange);font-weight:700;font-size:9px">NEXORA TECHNOLOGIES</div>
</section>

<section class="slide cover-logo" style="left:705px;top:15px">
  <div style="left:0;width:326px;top:46px;text-align:center;color:var(--orange);font-weight:700;font-size:36px;line-height:1">NEXORA</div>
  <div style="left:0;width:326px;top:84px;text-align:center;color:var(--orange);font-weight:700;font-size:9px;letter-spacing:6px">TECHNOLOGIES</div>
  <div style="left:0;top:131px;width:326px;height:38px;background:linear-gradient(#e3e3e3,#f1f1f1)"></div>
  <h1 class="h-slide" style="left:0;width:326px;top:136px;text-align:center;font-size:15px">PRESENTATION TITLE</h1>
  <div style="left:0;width:326px;top:151px;text-align:center;font-size:9px">Sub title goes here</div>
  <div style="left:0;top:169px;width:326px;height:15px;background:var(--orange)"></div>
</section>

<section class="slide agenda" style="left:16px;top:212px">
  <div class="mark">NEXORA</div>
  <div style="left:29px;top:0;width:70px;height:184px;background:var(--orange)"></div>
  <div class="vert" style="left:48px;top:144px;font-size:28px">Agenda</div>
  <div style="left:138px;top:20px;width:170px">
    <div style="margin-bottom:10px"><div style="font-size:8px;font-weight:700">Contents</div><p class="txt" style="color:var(--ink)">Get a modern presentation that is clean and well designed. I hope this template will save your time.</p></div>
    <div style="margin-bottom:10px"><div style="font-size:8px;font-weight:700">Contents</div><p class="txt" style="color:var(--ink)">Get a modern presentation that is clean and well designed. I hope this template will save your time.</p></div>
    <div style="margin-bottom:10px"><div style="font-size:8px;font-weight:700">Contents</div><p class="txt" style="color:var(--ink)">Get a modern presentation that is clean and well designed. I hope this template will save your time.</p></div>
    <div style="margin-bottom:10px"><div style="font-size:8px;font-weight:700">Contents</div><p class="txt" style="color:var(--ink)">Get a modern presentation that is clean and well designed. I hope this template will save your time.</p></div>
    <div><div style="font-size:8px;font-weight:700">Contents</div><p class="txt" style="color:var(--ink)">Get a modern presentation that is clean and well designed. I hope this template will save your time.</p></div>
  </div>
  <div class="footer">NEXORA TECHNOLOGIES<span class="pg">4</span></div>
</section>

<section class="slide welcome" style="left:361px;top:212px">
  <div class="mark">NEXORA</div>
  <div style="left:0;top:0;width:18px;height:184px;background:var(--orange)"></div>
  <h2 class="h-slide" style="left:37px;top:45px;font-size:13px">WELCOME</h2>
  <p class="txt" style="left:37px;top:63px;width:95px;color:var(--ink)">Lorem ipsum dolor sit amet, consectetur adipiscing elit, sed do eiusmod tempor incididunt ut labore et dolore magna aliqua. Lorem ipsum dolor sit amet, consectetur adipiscing elit, sed do eiusmod tempor incididunt ut labore et dolore magna aliqua. Ut enim ad minim veniam, quis nostrud exercitation ullamco laboris nisi ut aliquip lorem ipsum dolor sit amet, consectetur adipiscing elit, sed do eiusmod tempor incididunt ut labore et dolore magna aliqua.</p>
  <div style="left:163px;top:30px;width:58px;height:59px;background:var(--orange)"></div>
  <div class="photo" role="img" aria-label="Glowing blue network of connected computers" style="left:186px;top:46px;width:140px;height:99px;background:radial-gradient(ellipse at 50% 55%,#1e7ad8 0%,#0a2d6b 55%,#051535 100%);box-shadow:-3px 4px 6px rgba(0,0,0,.35)"></div>
  <div class="footer">NEXORA TECHNOLOGIES<span class="pg">5</span></div>
</section>

<section class="slide part-one" style="left:705px;top:212px">
  <div style="left:0;top:0;width:45px;height:184px;background:var(--orange)"></div>
  <div class="vert" style="left:10px;top:144px;font-size:20px">PART ONE</div>
  <div class="tab" style="left:145px;top:9px;width:26px;height:24px">01</div>
  <h2 class="h-slide" style="left:59px;top:41px;font-size:14px">ABOUT US</h2>
  <p class="txt" style="left:59px;top:59px;width:95px">Lorem ipsum dolor sit amet, consectetur adipiscing elit, sed do eiusmod tempor incididunt ut labore et dolore magna aliqua. Lorem ipsum dolor sit amet, consectetur adipiscing elit, sed do eiusmod tempor incididunt ut labore et dolore magna aliqua. Ut enim ad minim veniam, quis nostrud exercitation ullamco laboris nisi ut aliquip lorem ipsum dolor sit amet, consectetur adipiscing elit, sed do eiusmod tempor incididunt ut labore et dolore magna aliqua.</p>
  <div class="photo" role="img" aria-label="Glowing globe wrapped in a network mesh" style="left:171px;top:0;width:155px;height:178px;background:radial-gradient(circle at 55% 50%,#3c6a5a 0%,#1f2c4a 45%,#0c1020 75%,#5a3a18 100%)"></div>
  <div class="footer">NEXORA TECHNOLOGIES<span class="pg">6</span></div>
</section>

<section class="slide three-col" style="left:16px;top:410px">
  <div class="mark">NEXORA</div>
  <h2 class="h-slide" style="left:0;width:326px;top:18px;text-align:center;font-size:12px">YOUR TITLE GOES HERE</h2>
  <div style="left:17px;top:42px;width:93px">
    <p class="txt">Lorem ipsum dolor sit amet, consectetur adipiscing elit, sed do eiusmod tempor incididunt ut labore et dolore magna aliqua. Lorem ipsum dolor sit amet, consectetur adipiscing elit, sed do eiusmod tempor incididunt ut labore et dolore magna aliqua. Ut enim ad minim veniam, quis nostrud exercitation ullamco laboris nisi ut aliquip lorem ipsum dolor sit amet, consectetur adipiscing elit, sed do eiusmod tempor incididunt ut labore et dolore magna aliqua.</p>
    <ul class="bullets" style="margin-top:6px">
      <li>Lorem ipsum dolor enim sit amet, consectetur adipiscing elit, ma sed magna do eiusmod tempor</li>
      <li>Lorem ipsum dolor enim sit amet, consectetur adipiscing elit, ma sed magna do eiusmod tempor</li>
    </ul>
  </div>
  <p class="txt" style="left:121px;top:42px;width:91px">Lorem ipsum dolor sit amet, consectetur adipiscing elit, sed do eiusmod tempor incididunt ut labore et dolore magna aliqua. Lorem ipsum dolor sit amet, consectetur adipiscing elit, sed do eiusmod tempor incididunt ut labore et dolore magna aliqua. Ut enim ad minim veniam, quis nostrud exercitation ullamco laboris nisi ut aliquip lorem ipsum dolor sit amet, consectetur adipiscing elit, sed do eiusmod tempor incididunt ut labore et dolore magna aliqua. Quis nostrud exercitation ullamco laboris nisi ut aliquip lorem ipsum dolor sit amet, consectetur adipiscing elit, sed do eiusmod tempor incididunt ut labore et dolore magna aliqua.</p>
  <ul class="bullets" style="left:222px;top:44px;width:90px">
    <li style="margin-bottom:9px">Lorem ipsum dolor sit amet, consectetur adipiscing elit, sed do eiusmod tempor incididunt ut labore et dolore magna aliqua. Lorem ipsum dolor sit amet.</li>
    <li style="margin-bottom:9px">Consectetur adipiscing elit, sed do eiusmod tempor incididunt ut labore et dolore magna aliqua.</li>
    <li style="margin-bottom:9px">Ut enim ad minim veniam, quis nostrud exercitation ullamco laboris nisi ut aliquip.</li>
    <li>Lorem ipsum dolor sit amet, consectetur adipiscing elit, sed do eiusmod tempor incididunt ut labore et.</li>
  </ul>
  <div class="footer">NEXORA TECHNOLOGIES<span class="pg">7</span></div>
</section>

<section class="slide chart-slide" style="left:361px;top:410px">
  <div class="mark">NEXORA</div>
  <div style="left:8px;top:0;width:128px;height:30px;background:var(--orange)"></div>
  <div class="photo" role="img" aria-label="Hand touching a hexagon interface of IT topics" style="left:8px;top:36px;width:128px;height:142px;background:linear-gradient(135deg,#9aaab8 0%,#5c7086 45%,#2a3f5a 100%)"></div>
  <h2 class="h-slide" style="left:152px;top:25px;font-size:11.5px">Lorem ipsum dolor sit amet</h2>
  <p class="txt" style="left:152px;top:45px;width:162px;line-height:2.1">Lorem ipsum dolor sit amet, consectetuer adipiscing elit, sed diam nonummy nibh euismod tincidunt ut laoreet dolore magna aliquam erat volutpat. Ut wisi enim ad minim veniam, quis nostrud exerci tation ullamcorper suscipit lobortis nisl ut aliquip ex ea commodo consequat.</p>
  <svg style="left:140px;top:84px" width="176" height="90" font-size="3" fill="#666">
    <g stroke="#e2e2e2" stroke-width=".4">
      <line x1="14" y1="4" x2="174" y2="4"/>
      <line x1="14" y1="11.3" x2="174" y2="11.3"/><line x1="14" y1="18.6" x2="174" y2="18.6"/><line x1="14" y1="25.9" x2="174" y2="25.9"/><line x1="14" y1="33.2" x2="174" y2="33.2"/><line x1="14" y1="40.5" x2="174" y2="40.5"/><line x1="14" y1="47.8" x2="174" y2="47.8"/><line x1="14" y1="55.1" x2="174" y2="55.1"/><line x1="14" y1="62.4" x2="174" y2="62.4"/><line x1="14" y1="69.7" x2="174" y2="69.7"/><line x1="14" y1="77" x2="174" y2="77"/>
    </g>
    <text x="6" y="5">5</text><text x="6" y="19.6">4</text><text x="6" y="34.2">3</text><text x="6" y="48.8">2</text><text x="6" y="63.4">1</text><text x="6" y="78">0</text>
    <rect x="20" y="14" width="5" height="63" fill="var(--orange)"/><rect x="27" y="42" width="5" height="35" fill="var(--dark)"/><rect x="34" y="48" width="5" height="29" fill="#2f74c0"/>
    <rect x="59" y="40.5" width="5" height="36.5" fill="var(--orange)"/><rect x="66" y="13" width="5" height="64" fill="var(--dark)"/><rect x="73" y="48" width="5" height="29" fill="#2f74c0"/>
    <rect x="98" y="26" width="5" height="51" fill="var(--orange)"/><rect x="105" y="51" width="5" height="26" fill="var(--dark)"/><rect x="112" y="33" width="5" height="44" fill="#2f74c0"/>
    <rect x="137" y="11" width="5" height="66" fill="var(--orange)"/><rect x="144" y="36" width="5" height="41" fill="var(--dark)"/><rect x="151" y="4" width="5" height="73" fill="#2f74c0"/>
    <text x="22" y="85">Category 1</text><text x="61" y="85">Category 2</text><text x="100" y="85">Category 3</text><text x="139" y="85">Category 4</text>
  </svg>
  <div class="footer">NEXORA TECHNOLOGIES<span class="pg">8</span></div>
</section>

<section class="slide split-orange" style="left:705px;top:410px">
  <div class="mark">NEXORA</div>
  <div style="left:0;top:12px;width:19px;height:63px;background:var(--orange)"></div>
  <div style="left:207px;top:0;width:83px;height:178px;background:var(--orange)"></div>
  <h2 class="h-slide" style="left:33px;top:28px;font-size:13px">Lorem ipsum dolor</h2>
  <p class="txt" style="left:33px;top:50px;width:122px;line-height:2.3">Ut wisi enim ad minim veniam, quis nostrud exerci tation ullamcorper suscipit lobortis nisl ut aliquip ex ea commodo consequat. Lorem ipsum dolor sit amet, consectetuer adipiscing elit, sed diam nonummy nibh euismod tincidunt ut laoreet dolore magna aliquam erat volutpat. Ut wisi enim ad minim veniam, quis nostrud exerci tation ullamcorper suscipit lobortis nisl ut aliquip ex ea commodo consequat.</p>
  <div class="photo" role="img" aria-label="Hands holding a tablet with glowing app icons" style="left:211px;top:44px;width:107px;height:93px;background:linear-gradient(160deg,#c9c9c9 0%,#6d6d6d 50%,#2a2a2a 100%)"></div>
  <div style="left:33px;top:128px;width:50px"><div style="font-size:3.8px;font-weight:700">LOREM IPSUM DOLOR</div><p class="txt" style="margin-top:2px">Lorem ipsum dolor sit amet, nec an dictas equidem appellantur, ut has commune accommo. Mea illum corrupit gloriatur et ludus.</p></div>
  <div style="left:93px;top:128px;width:50px"><div style="font-size:3.8px;font-weight:700">LOREM IPSUM DOLOR</div><p class="txt" style="margin-top:2px">Lorem ipsum dolor sit amet, nec an dictas equidem appellantur, ut has commune accome. Mea illum corrupit gloriatur et ludus.</p></div>
  <div style="left:152px;top:128px;width:50px"><div style="font-size:3.8px;font-weight:700">LOREM IPSUM DOLOR</div><p class="txt" style="margin-top:2px">Lorem ipsum dolor sit amet, nec an dictas equidem appellantur, ut has commune accodare. Mea illum corrupit gloriatur et ludus.</p></div>
  <div class="footer">NEXORA TECHNOLOGIES<span class="pg">9</span></div>
</section>

<section class="slide part-two" style="left:16px;top:608px">
  <div style="left:0;top:0;width:45px;height:184px;background:var(--orange)"></div>
  <div class="vert" style="left:10px;top:144px;font-size:20px">PART TWO</div>
  <div class="tab" style="left:143px;top:8px;width:34px;height:24px">02</div>
  <h2 class="h-slide" style="left:59px;top:42px;font-size:14px">Lorem ipsum<br>dolor sit amet</h2>
  <p class="txt" style="left:59px;top:76px;width:95px">Lorem ipsum dolor sit amet, consectetur adipiscing elit, sed do eiusmod tempor incididunt ut labore et dolore magna aliqua. Lorem ipsum dolor sit amet, consectetur adipiscing elit, sed do eiusmod tempor incididunt ut labore et dolore magna aliqua. Ut enim ad minim veniam, quis nostrud exercitation ullamco laboris nisi ut aliquip lorem ipsum dolor sit amet, consectetur adipiscing elit, sed do eiusmod tempor incididunt ut labore et dolore magna aliqua.</p>
  <div class="photo" role="img" aria-label="Glowing golden circuit board traces" style="left:177px;top:0;width:149px;height:184px;background:radial-gradient(ellipse at 55% 45%,#c99a2a 0%,#5a4a22 30%,#14202c 70%,#0a0f18 100%)"></div>
  <div class="footer" style="background:transparent"><span style="position:absolute;left:0;width:177px;height:6px;background:var(--orange)">NEXORA TECHNOLOGIES</span></div>
</section>

<section class="slide feature-cards" style="left:361px;top:608px">
  <div class="mark">NEXORA</div>
  <h2 class="h-slide" style="left:0;width:326px;top:22px;text-align:center;font-size:15px">Lorem ipsum dolor</h2>
  <p class="txt" style="left:24px;top:52px;width:278px;text-align:center;font-size:4px;line-height:1.6;color:var(--ink)">Lorem ipsum dolor sit amet, consectetur adipiscing elit, sed do eiusmod tempor incididunt ut labore et dolore magna aliqua. Lorem ipsum dolor sit amet, consectetur adipiscing elit, sed do eiusmod tempor incididunt ut labore et dolore magna aliqua. Ut enim ad minim veniam, quis nostrud exercitation ullamco laboris nisi ut aliquip lorem ipsum dolor sit amet, consectetur adipiscing elit, sed do eiusmod tempor incididunt ut labore et dolore magna aliqua.</p>
  <div style="left:0;top:119px;width:326px;height:59px;background:var(--dark)"></div>
  <div style="left:20px;top:87px;width:78px;height:77px;border-radius:8px;background:var(--orange)"></div>
  <div style="left:120px;top:87px;width:79px;height:77px;border-radius:8px;background:var(--orange)"></div>
  <div style="left:220px;top:87px;width:78px;height:77px;border-radius:8px;background:var(--orange)"></div>
  <svg style="left:49px;top:93px" width="20" height="26" fill="none" stroke="#fff" stroke-width="1.5"><rect x="4" y="1" width="12" height="22" rx="2"/><line x1="8" y1="19" x2="12" y2="19"/></svg>
  <svg style="left:148px;top:96px" width="24" height="20" fill="none" stroke="#fff" stroke-width="1.5"><rect x="4" y="2" width="16" height="11" rx="1"/><line x1="1" y1="16" x2="23" y2="16"/></svg>
  <svg style="left:247px;top:94px" width="24" height="24" fill="none" stroke="#fff" stroke-width="1.4"><rect x="2" y="8" width="10" height="13"/><line x1="4" y1="12" x2="10" y2="12"/><line x1="4" y1="15" x2="10" y2="15"/><circle cx="15" cy="9" r="7" fill="#fff"/></svg>
  <p class="txt" style="left:24px;top:130px;width:70px;color:#fff;text-align:center">Lorem ipsum dolor sit amet, consectetur adipiscing elit, sed do eiusmod tempor incididunt ut labore et dolore magna aliqua.</p>
  <p class="txt" style="left:125px;top:130px;width:70px;color:#fff;text-align:center">Lorem ipsum dolor sit amet, consectetur adipiscing elit, sed do eiusmod tempor incididunt ut labore et dolore magna aliqua.</p>
  <p class="txt" style="left:224px;top:130px;width:70px;color:#fff;text-align:center">Lorem ipsum dolor sit amet, consectetur adipiscing elit, sed do eiusmod tempor incididunt ut labore et dolore magna aliqua.</p>
  <div class="footer">NEXORA TECHNOLOGIES<span class="pg">11</span></div>
</section>

<section class="slide image-panels" style="left:705px;top:608px">
  <div class="mark">NEXORA</div>
  <h2 class="h-slide" style="left:0;width:326px;top:12px;text-align:center;font-size:15px">Lorem ipsum dolor</h2>
  <div class="photo" role="img" aria-label="Hand surrounded by floating communication icons" style="left:15px;top:32px;width:95px;height:134px;background:radial-gradient(ellipse at 50% 55%,#6fa6d8 0%,#2e5a8e 50%,#142a4a 100%)"></div>
  <div style="left:114px;top:32px;width:95px;height:134px;background:var(--orange)"></div>
  <div style="left:213px;top:32px;width:96px;height:134px;background:var(--orange)"></div>
  <svg style="left:153px;top:40px" width="18" height="18" fill="none" stroke="#fff" stroke-width="2"><circle cx="9" cy="9" r="4"/><circle cx="9" cy="9" r="7" stroke-dasharray="2.5 2"/></svg>
  <svg style="left:252px;top:40px" width="18" height="18" fill="none" stroke="#fff" stroke-width="2"><circle cx="7" cy="7" r="5"/><line x1="11" y1="11" x2="16" y2="16"/></svg>
  <div style="left:114px;width:95px;top:65px;text-align:center;color:#fff;font-size:5px;font-weight:700">Lorem ipsum dolor sit amet</div>
  <div style="left:213px;width:96px;top:65px;text-align:center;color:#fff;font-size:5px;font-weight:700">Lorem ipsum dolor sit amet</div>
  <p class="txt" style="left:120px;top:79px;width:83px;color:#fff;text-align:center;line-height:2.2">Lorem ipsum dolor sit amet, consectetur adipiscing elit, sed do eiusmod tempor incididunt ut labore et dolore magna aliqua. Ut enim ad minim veniam, quis nostrud exercitation ullamco laboris nisi ut aliquip ex. Lorem ipsum dolor sit amet, consectetur adipiscing elit, sed do eiusmod tempor incididunt ut labore et dolore magna aliqua.</p>
  <p class="txt" style="left:219px;top:79px;width:84px;color:#fff;text-align:center;line-height:2.2">Lorem ipsum dolor sit amet, consectetur adipiscing elit, sed do eiusmod tempor incididunt ut labore et dolore magna aliqua. Ut enim ad minim veniam, quis nostrud exercitation ullamco laboris nisi ut aliquip ex. Lorem ipsum dolor sit amet, consectetur adipiscing elit, sed do eiusmod tempor incididunt ut labore et dolore magna aliqua.</p>
  <div class="footer">NEXORA TECHNOLOGIES<span class="pg">12</span></div>
</section>

<section class="slide data-table" style="left:16px;top:806px">
  <div class="mark">NEXORA</div>
  <h2 class="h-slide" style="left:0;width:326px;top:22px;text-align:center;font-size:15px">Lorem ipsum dolor</h2>
  <svg style="left:0;top:48px" width="326" height="118" font-size="4.2" text-anchor="middle" fill="#222">
    <rect x="105" y="0" width="55" height="22" fill="var(--orange)"/><rect x="160" y="0" width="54" height="22" fill="var(--dark)"/><rect x="214" y="0" width="55" height="22" fill="var(--orange)"/><rect x="269" y="0" width="57" height="22" fill="var(--dark)"/>
    <g fill="#fff" font-size="3.6" font-weight="700"><text x="132" y="9">Lorem ipsum dolor sit</text><text x="132" y="14">amet</text><text x="187" y="9">Lorem ipsum dolor sit</text><text x="187" y="14">amet</text><text x="241" y="9">Lorem ipsum dolor sit</text><text x="241" y="14">amet</text><text x="297" y="9">Lorem ipsum dolor sit</text><text x="297" y="14">amet</text></g>
    <rect x="0" y="22" width="326" height="15.7" fill="var(--grey-light)"/><rect x="0" y="37.7" width="326" height="15.7" fill="var(--grey)"/><rect x="0" y="53.4" width="326" height="15.7" fill="var(--grey-light)"/><rect x="0" y="69.1" width="326" height="15.7" fill="var(--grey)"/><rect x="0" y="84.8" width="326" height="15.7" fill="var(--grey-light)"/><rect x="0" y="100.5" width="326" height="15.7" fill="var(--grey)"/>
    <g stroke="#fff" stroke-width=".6"><line x1="105" y1="22" x2="105" y2="116"/><line x1="160" y1="22" x2="160" y2="116"/><line x1="214" y1="22" x2="214" y2="116"/><line x1="269" y1="22" x2="269" y2="116"/></g>
    <text x="52" y="31.5">Lorem ipsum dolor</text><text x="132" y="31.5">23</text><text x="187" y="31.5">45</text><text x="241" y="31.5">4</text><text x="297" y="31.5">4</text>
    <text x="52" y="47.2">Lorem ipsum dolor</text><text x="132" y="47.2">234</text><text x="187" y="47.2">75</text><text x="241" y="47.2">4</text><text x="297" y="47.2">4</text>
    <text x="52" y="62.9">Lorem ipsum dolor</text><text x="132" y="62.9">55</text><text x="187" y="62.9">75</text><text x="241" y="62.9">64</text><text x="297" y="62.9">6</text>
    <text x="52" y="78.6">Lorem ipsum dolor</text><text x="132" y="78.6">66</text><text x="187" y="78.6">45</text><text x="241" y="78.6">4</text><text x="297" y="78.6">4</text>
    <text x="52" y="94.3">Lorem ipsum dolor</text><text x="132" y="94.3">78</text><text x="187" y="94.3">64</text><text x="241" y="94.3">46</text><text x="297" y="94.3">6</text>
    <text x="52" y="110">Lorem ipsum dolor</text><text x="132" y="110">56</text><text x="187" y="110">46</text><text x="241" y="110">44</text><text x="297" y="110">3</text>
  </svg>
  <div class="footer">NEXORA TECHNOLOGIES<span class="pg">13</span></div>
</section>

<section class="slide pricing" style="left:361px;top:806px">
  <div class="mark">NEXORA</div>
  <h2 class="h-slide" style="left:0;width:326px;top:22px;text-align:center;font-size:15px">Lorem ipsum dolor</h2>
  <svg style="left:0;top:48px" width="326" height="112" font-size="4.2" text-anchor="middle">
    <g fill="var(--orange)"><rect x="47" y="0" width="51" height="15"/><rect x="104" y="0" width="52" height="15"/><rect x="161" y="0" width="52" height="15"/><rect x="220" y="0" width="51" height="15"/></g>
    <g fill="#fff" font-weight="700" font-size="4.5"><text x="72.5" y="9.5">FREE</text><text x="130" y="9.5">STANDARD</text><text x="187" y="9.5">PROFESSIONAL</text><text x="245.5" y="9.5">PRO UNLIMITED</text></g>
    <g fill="#f6f6f6"><rect x="47" y="15" width="51" height="60"/><rect x="104" y="15" width="52" height="60"/><rect x="161" y="15" width="52" height="60"/><rect x="220" y="15" width="51" height="60"/></g>
    <g fill="#dfe3e8"><rect x="47" y="79" width="51" height="9"/><rect x="104" y="79" width="52" height="9"/><rect x="161" y="79" width="52" height="9"/><rect x="220" y="79" width="51" height="9"/></g>
    <g fill="#eef0f3"><rect x="47" y="88" width="51" height="22"/><rect x="104" y="88" width="52" height="22"/><rect x="161" y="88" width="52" height="22"/><rect x="220" y="88" width="51" height="22"/></g>
    <g fill="#777" font-size="3.6"><text x="72.5" y="85">Price:</text><text x="130" y="85">Price:</text><text x="187" y="85">Price:</text><text x="245.5" y="85">Price:</text></g>
    <g fill="#333" font-size="6"><text x="72.5" y="101">Free</text><text x="130" y="101">$ 19</text><text x="187" y="101">$ 49</text><text x="245.5" y="101">$ 99</text></g>
  </svg>
  <ul class="bullets" style="left:50px;top:67px;width:46px"><li style="padding-left:5px;font-size:3px;margin-bottom:3px">Lorem ipsum dolor sit amet, nec an dictas equidem</li><li style="padding-left:5px;font-size:3px;margin-bottom:3px">Ut has commune accommodare</li><li style="padding-left:5px;font-size:3px">Mea illum corrupit gloriatur et, ludus solet id pro.</li></ul>
  <ul class="bullets" style="left:107px;top:67px;width:46px"><li style="padding-left:5px;font-size:3px;margin-bottom:3px">Lorem ipsum dolor sit amet, nec an dictas equidem</li><li style="padding-left:5px;font-size:3px;margin-bottom:3px">Ut has commune accommodare</li><li style="padding-left:5px;font-size:3px">Mea illum corrupit gloriatur et, ludus solet id pro.</li></ul>
  <ul class="bullets" style="left:164px;top:67px;width:46px"><li style="padding-left:5px;font-size:3px;margin-bottom:3px">Lorem ipsum dolor sit amet, nec an dictas equidem</li><li style="padding-left:5px;font-size:3px;margin-bottom:3px">Ut has commune accommodare</li><li style="padding-left:5px;font-size:3px">Mea illum corrupit gloriatur et, ludus solet id pro.</li></ul>
  <ul class="bullets" style="left:223px;top:67px;width:46px"><li style="padding-left:5px;font-size:3px;margin-bottom:3px">Lorem ipsum dolor sit amet, nec an dictas equidem</li><li style="padding-left:5px;font-size:3px;margin-bottom:3px">Ut has commune accommodare</li><li style="padding-left:5px;font-size:3px">Mea illum corrupit gloriatur et, ludus solet id pro.</li></ul>
  <div class="footer">NEXORA TECHNOLOGIES<span class="pg">14</span></div>
</section>

<section class="slide puzzle" style="left:705px;top:806px">
  <div class="mark">NEXORA</div>
  <h2 class="h-slide" style="left:0;width:326px;top:14px;text-align:center;font-size:15px">Lorem ipsum dolor</h2>
  <div class="photo" role="img" aria-label="Four jigsaw puzzle pieces in orange, grey and black joined in a cycle with arrows" style="left:102px;top:40px;width:122px;height:122px;border-radius:6px;background:linear-gradient(135deg,#f8b27a 0%,var(--orange) 40%,#9a9a9a 70%,var(--dark) 100%)"></div>
  <div style="left:20px;top:41px;width:72px"><div style="font-size:5px;font-weight:700">Lorem Ipsum Dolor sit</div><p class="txt" style="margin-top:2px;text-align:left">Lorem ipsum dolor sit amet, nec an dictas equidem appellantur, ut has commune accommodare. Mea illum, ludus solet idpro.</p></div>
  <div style="left:234px;top:41px;width:72px;text-align:right"><div style="font-size:5px;font-weight:700">Lorem Ipsum Dolor sit</div><p class="txt" style="margin-top:2px;text-align:right">Lorem ipsum dolor sit amet, nec an dictas equidem appellantur, ut has commune accommodare. Mea illum, ludus solet idpro.</p></div>
  <div style="left:20px;top:126px;width:72px"><div style="font-size:5px;font-weight:700">Lorem Ipsum Dolor sit</div><p class="txt" style="margin-top:2px;text-align:left">Lorem ipsum dolor sit amet, nec an dictas equidem appellantur, ut has commune accommodare. Mea illum, ludus solet idpro.</p></div>
  <div style="left:234px;top:126px;width:72px;text-align:right"><div style="font-size:5px;font-weight:700">Lorem Ipsum Dolor sit</div><p class="txt" style="margin-top:2px;text-align:right">Lorem ipsum dolor sit amet, nec an dictas equidem appellantur, ut has commune accommodare. Mea illum, ludus solet idpro.</p></div>
  <div class="footer">NEXORA TECHNOLOGIES<span class="pg">15</span></div>
</section>

<section class="slide content-boxes" style="left:179px;top:1003px">
  <div class="mark">NEXORA</div>
  <div style="left:0;top:34px;width:16px;height:116px;background:var(--orange)"></div>
  <h2 class="h-slide" style="left:29px;top:37px;font-size:14px">Lorem ipsum<br>dolor sit amet</h2>
  <p class="txt" style="left:29px;top:71px;width:94px">Lorem ipsum dolor sit amet, consectetur adipiscing elit, sed do eiusmod tempor incididunt ut labore et dolore magna aliqua. Lorem ipsum dolor sit amet, consectetur adipiscing elit, sed do eiusmod tempor incididunt ut labore et dolore magna aliqua. Ut enim ad minim veniam, quis nostrud exercitation ullamco laboris nisi ut aliquip lorem ipsum dolor sit amet, consectetur adipiscing elit, sed do eiusmod tempor incididunt ut labore et dolore magna aliqua.</p>
  <div class="box-head" style="left:153px;top:32px;width:71px">Your Contents Here</div>
  <div class="box-head" style="left:230px;top:32px;width:72px">Your Contents Here</div>
  <div class="box-head" style="left:153px;top:94px;width:71px">Your Contents Here</div>
  <div class="box-head" style="left:230px;top:94px;width:72px">Your Contents Here</div>
  <p class="txt box-body" style="left:155px;top:43px;width:66px">Lorem ipsum dolor sit amet, consectetur adipiscing elit, sed do eiusmod tempor incididunt ut labore et dolore magna aliqua. Lorem ipsum dolor sit amet, consectetur adipiscing elit.</p>
  <p class="txt box-body" style="left:232px;top:43px;width:67px">Lorem ipsum dolor sit amet, consectetur adipiscing elit, sed do eiusmod tempor incididunt ut labore et dolore magna aliqua. Lorem ipsum dolor sit amet, consectetur adipiscing elit.</p>
  <p class="txt box-body" style="left:155px;top:105px;width:66px">Lorem ipsum dolor sit amet, consectetur adipiscing elit, sed do eiusmod tempor incididunt ut labore et dolore magna aliqua. Lorem ipsum dolor sit amet, consectetur adipiscing elit.</p>
  <p class="txt box-body" style="left:232px;top:105px;width:67px">Lorem ipsum dolor sit amet, consectetur adipiscing elit, sed do eiusmod tempor incididunt ut labore et dolore magna aliqua. Lorem ipsum dolor sit amet, consectetur adipiscing elit.</p>
  <div class="footer">NEXORA TECHNOLOGIES<span class="pg">16</span></div>
</section>

<section class="slide contact" style="left:524px;top:1003px">
  <div class="mark">NEXORA</div>
  <svg style="left:0;top:0" width="190" height="184"><path d="M0 0 H105 C150 0 182 40 182 90 C182 140 150 178 105 178 H0 Z" fill="var(--dark)"/></svg>
  <div style="left:0;width:164px;top:65px;text-align:center;color:#fff;font-weight:700;font-size:29px;line-height:1">NEXORA</div>
  <div style="left:0;width:164px;top:100px;text-align:center;color:var(--orange);font-weight:700;font-size:15px">Get in Touch</div>
  <svg style="left:214px;top:33px" width="14" height="14" fill="var(--orange)"><path d="M3 1 L6 1 L7 4 L5 6 Q7 9 9 10 L11 8 L14 9 L14 12 Q13 14 11 14 Q1 12 1 3 Q1 1 3 1 Z"/></svg>
  <div style="left:236px;top:37px;font-size:5.5px">555.010.2040</div>
  <svg style="left:214px;top:63px" width="16" height="16" fill="none" stroke="var(--orange)" stroke-width="1.2"><circle cx="8" cy="8" r="7"/><ellipse cx="8" cy="8" rx="3" ry="7"/><line x1="1" y1="8" x2="15" y2="8"/><line x1="2.5" y1="4.5" x2="13.5" y2="4.5"/><line x1="2.5" y1="11.5" x2="13.5" y2="11.5"/></svg>
  <div style="left:236px;top:68px;font-size:5.5px">www.nexora-tech.example</div>
  <svg style="left:214px;top:94px" width="18" height="13"><rect x="0" y="0" width="18" height="13" rx="1" fill="var(--orange)"/><path d="M1 1 L9 7 L17 1" fill="none" stroke="#fff" stroke-width="1.2"/></svg>
  <div style="left:238px;top:97px;font-size:5.5px">info@nexora-tech.example</div>
  <svg style="left:216px;top:123px" width="14" height="18" fill="var(--orange)"><path d="M7 0 C11 0 14 3 14 7 C14 11 7 18 7 18 C7 18 0 11 0 7 C0 3 3 0 7 0 Z"/><circle cx="7" cy="7" r="2.5" fill="#fff"/></svg>
  <div style="left:236px;top:126px;font-size:5.5px;text-align:center;line-height:1.4">Here to write your,<br>Company adress</div>
  <div class="footer">NEXORA TECHNOLOGIES<span class="pg">17</span></div>
</section>

<div class="dot" style="left:888px;top:1016px;background:var(--orange)"></div>
<div class="dot" style="left:927px;top:1016px;background:var(--grey)"></div>
<div class="dot" style="left:967px;top:1016px;background:var(--dark)"></div>

</body>
</html>
```